Webdesign für Gemeinschaftspraxis (13820)
Zielgruppe
Die Website ist für eine fachärztliche Gemeinschaftspraxis, die sich aus Internisten, Betriebsmedizinern, Präventionsärzten, Kardiologen, Allgemeinmedizinern und Phlebologen zusammensetzt.
Die Zielgruppe sind bestehende Patienten sowie potentielle Patienten.
Die Website soll informativ sein.
Aufgabenstellung
Die Website soll in schlichten Farben gehalten sein, die zum Logo und zu den Fotos passen.
Die Website soll als kurzer, informativer Auftritt dienen
Die gelieferten Fotos sollen verwendet werden.
Es soll eine Onepage-Website werden, die so aufgebaut ist, wie die Website unter dem folgenden Link: https://www.kolbenfeld-portal.de/

```html
<!DOCTYPE html>
<html lang="de">
<head>
<meta charset="utf-8">
<title>Praxisgemeinschaft Harlen</title>
<link href="https://fonts.googleapis.com/css2?family=Roboto:wght@300;400;500;700&family=Open+Sans:ital,wght@0,400;0,600;0,700;1,400&display=swap" rel="stylesheet">
<style>
:root{
  --navy:#1b2a55;
  --blue:#3a5bb5;
  --blue-mid:#2d4a8a;
  --blue-light:#6a86d6;
  --text:#4b4f5c;
  --muted:#9aa0ad;
  --bg-soft:#f7f7f9;
  --purple:#b463c8;
  --slate:#8ea2ba;
  --rose:#e99495;
  --dusk:#5e6f92;
  --sky:#7d9bd3;
  --green:#6fbf9e;
  --button:#7c9bd0;
  --footer-text:#7386b8;
}
*{margin:0;padding:0;box-sizing:border-box}
html,body{width:1200px;height:3873px;overflow:hidden}
body{position:relative;font-family:"Open Sans",sans-serif;color:var(--text);background:#fff}
.abs{position:absolute}

/* hero */
.hero{left:0;top:0;width:1200px;height:632px;overflow:hidden}
.hero-photo{position:absolute;inset:0;background:linear-gradient(110deg,#c9b9a3 0%,#e9e3da 35%,#f4f1ec 55%,#d9c3a0 70%,#efe9e1 100%)}
.hero-shapes{position:absolute;inset:0}
.nav{position:absolute;left:471px;top:26px;width:729px;height:57px;background:var(--navy);display:flex;align-items:center;justify-content:flex-end;padding-right:110px;gap:30px}
.nav a{color:#fff;text-decoration:none;font:700 11.5px "Open Sans",sans-serif;letter-spacing:.3px}
.brand{position:absolute;left:111px;top:0;width:233px;height:150px;background:#fff;display:flex;flex-direction:column;align-items:center;justify-content:center;gap:8px}
.brand-mark{width:26px;height:26px;background:var(--navy)}
.brand-name{font:600 13px "Open Sans",sans-serif;color:var(--navy);text-align:center;line-height:1.35}
.brand-name small{font-size:10px}
.hero-band{position:absolute;left:632px;top:447px;width:568px;height:90px;background:rgba(255,255,255,.55)}
.hero-title{position:absolute;right:110px;top:447px;text-align:right;color:var(--navy)}
.hero-title h1{font:700 43px "Roboto",sans-serif;letter-spacing:1px;line-height:1.05}
.hero-title p{font:400 31px "Roboto",sans-serif;letter-spacing:1.5px;line-height:1.1}

/* headings */
.section-title{font:400 32px "Roboto",sans-serif;color:var(--navy);letter-spacing:2px;text-align:center;width:1200px;left:0}

/* services */
.services{left:0;top:632px;width:1200px;height:744px;background:#fff}
.services-bg{left:0;top:1336px;width:1200px;height:40px;background:var(--bg-soft)}
.services .lead{position:absolute;top:122px;width:1200px;text-align:center;font:italic 14.5px/22px "Open Sans",sans-serif;color:var(--text)}
.service-box{position:absolute;left:111px;top:204px;width:976px;height:453px;border:1.5px solid var(--blue-mid);display:flex}
.service-menu{width:318px;background:var(--navy);list-style:none;position:relative}
.service-menu li{height:62px;display:flex;align-items:center;padding:0 12px;color:#d7dcec;font:600 12.5px/20px "Open Sans",sans-serif;border-bottom:1px solid #2c3c6d;letter-spacing:.2px}
.service-menu li.active{background:var(--blue-mid);color:#fff}
.service-menu .scroll{position:absolute;right:0;top:0;width:8px;height:100%;background:#243463}
.service-menu .scroll i{position:absolute;left:0;top:70px;width:8px;height:170px;background:#4c65b0}
.service-body{flex:1;padding:30px 26px 0 26px;position:relative}
.service-body h3{font:500 17px "Roboto",sans-serif;color:var(--navy);letter-spacing:.5px;margin-bottom:12px}
.service-body p{font:400 12.5px/22px "Open Sans",sans-serif;color:var(--text);margin-bottom:22px}
.service-body .intro{width:352px}
.service-photo{position:absolute;right:24px;top:35px;width:232px;height:203px;background:linear-gradient(135deg,#f1ede6 0%,#e7ddd1 45%,#2f5fc4 80%,#1f4aa8 100%)}

/* doctors */
.doctors{left:0;top:1376px;width:1200px;height:609px;background:#fff}
.doctor{position:absolute;top:120px;width:308px;height:411px;background:#fff;box-shadow:0 2px 14px rgba(27,42,85,.09);text-align:center}
.doctor .portrait{width:134px;height:135px;margin:43px auto 0;border:1.5px solid #6a9fd6;padding:3px}
.doctor .portrait div{width:100%;height:100%;background:linear-gradient(180deg,#9ea3a8,#6e6a66)}
.doctor h4{font:600 16px "Open Sans",sans-serif;color:#2a2d36;margin-top:25px}
.doctor .role{font:400 11px "Open Sans",sans-serif;color:var(--muted);margin-top:4px}
.doctor p{font:400 13px/22.5px "Open Sans",sans-serif;color:var(--text);margin:14px auto 0;width:236px}

/* hours */
.hours{left:0;top:1985px;width:1200px;height:903px}
.hours-bg{position:absolute;inset:0;background:linear-gradient(160deg,#e7e9ee 0%,#d9dde4 40%,#cdd2da 70%,#e2e5ea 100%)}
.hours .section-title{top:48px;color:var(--blue-mid)}
.schedule{position:absolute;left:111px;top:98px;width:976px;border-collapse:collapse;table-layout:fixed}
.schedule th,.schedule td{color:#fff;font:600 14.5px/19px "Open Sans",sans-serif;text-align:left;vertical-align:top;border-right:1px solid rgba(255,255,255,.35);border-bottom:1px solid rgba(255,255,255,.35);padding:0 0 0 17px}
.schedule th{background:var(--blue);height:42px;vertical-align:middle;font-weight:700;font-size:14px}
.schedule td{height:64.3px;padding-top:12px}
.schedule td.time{background:var(--blue-light);padding-left:23px}
.c-blood{background:var(--purple)}
.c-free{background:var(--slate)}
.c-visit{background:var(--rose)}
.c-lunch{background:var(--dusk)}
.c-appt{background:var(--sky)}
.c-late{background:var(--green)}

/* team */
.team{left:0;top:2888px;width:1200px;height:631px;background:#fff}
.team-photo{position:absolute;left:113px;top:112px;width:400px;height:519px;background:linear-gradient(180deg,#eef2fa 0%,#dde5f5 45%,#5b83d4 75%,#2a57b8 100%)}
.team h2{position:absolute;left:531px;top:92px;font:400 31px "Roboto",sans-serif;color:var(--navy);letter-spacing:1.5px}
.slider-line{position:absolute;left:805px;top:110px;width:198px;height:1px;background:#d6d9e0}
.slider-dot{position:absolute;left:797px;top:105px;width:10px;height:10px;border:1px solid #cfd3dc;border-radius:50%;background:#fff}
.arrow{position:absolute;top:94px;width:33px;height:33px;display:flex;align-items:center;justify-content:center}
.arrow.prev{left:1020px;background:var(--navy)}
.arrow.next{left:1054px;background:#e4e6eb}
.member{position:absolute;left:531px;top:168px;width:560px}
.member h3{font:400 20px "Roboto",sans-serif;color:#2a2d36;letter-spacing:.5px}
.member .role{font:italic 12px "Open Sans",sans-serif;color:#6b6f7a;margin-top:4px}
.member p{font:400 12.8px/22.3px "Open Sans",sans-serif;color:var(--text);margin-top:23px}
.member p+p{margin-top:22px}

/* footer */
.footer{left:0;top:3519px;width:1200px;height:354px;background:var(--navy)}
.footer h2{position:absolute;top:70px;font:400 31px "Roboto",sans-serif;color:#4f6fb8;letter-spacing:1px}
.contact-line{position:absolute;font:400 12px "Open Sans",sans-serif;color:var(--footer-text);display:flex;align-items:center;gap:10px}
.legal{position:absolute;font:400 11.5px "Open Sans",sans-serif;color:var(--footer-text);white-space:nowrap}
.field{position:absolute;background:#2a3c6f;height:48px;padding-left:16px;display:flex;align-items:center;font:italic 13px "Open Sans",sans-serif;color:#6f82b4}
.submit{position:absolute;left:614px;top:239px;width:473px;height:48px;background:var(--button);color:var(--navy);font:600 14px "Roboto",sans-serif;letter-spacing:2px;display:flex;align-items:center;justify-content:center}
</style>
</head>
<body>

<header class="abs hero">
  <div class="hero-photo" role="img" aria-label="Foto des hellen Praxisempfangs mit Holztresen und Blumen"></div>
  <svg class="hero-shapes" width="1200" height="632" viewBox="0 0 1200 632">
    <polygon points="0,0 520,0 0,190" fill="#ffffff"/>
    <polygon points="0,190 0,632 640,632" fill="#1b2a55"/>
  </svg>
  <div class="brand">
    <div class="brand-mark"></div>
    <div class="brand-name">Praxisgemeinschaft Harlen<br><small>Dr. Borwig · Dr. Kessel · Andrae</small></div>
  </div>
  <nav class="nav">
    <a>HOME</a><a>DIENSTLEISTUNGEN</a><a>UNSER TEAM</a><a>ÖFFNUNGSZEITEN</a><a>KONTAKTIERE UNS</a>
  </nav>
  <div class="hero-band"></div>
  <div class="hero-title">
    <h1>SED UT PERSPICIATIS</h1>
    <p>UNDE OMNIS ISTE NATUS</p>
  </div>
</header>

<section class="abs services">
  <h2 class="abs section-title" style="top:77px">UNSERE DIENSTLEISTUNGEN</h2>
  <p class="lead">Nemo enim ipsam voluptatem quia voluptas sit aspernatur aut odit aut fugit, sed quia<br>consequuntur magni dolores eos qui ratione voluptatem sequi nesciunt.</p>
  <div class="service-box">
    <ul class="service-menu">
      <li style="height:86px">GESUNDHEITSVORSORGE<br>/PRÄVENTION/ GESUNDHEITS-CHECK-UP</li>
      <li>IMPFUNGEN UND REISEIMPFUNGEN</li>
      <li class="active">MÄNNERVORSORGE</li>
      <li>DIABETES MELLITUS</li>
      <li>PSYCHOSOMATISCHE GRUNDVERSORGUNG</li>
      <li>KORONARE HERZERKRANKUNG (KHK)</li>
      <li style="border-bottom:0">ASTHMA BRONCHIAL</li>
      <span class="scroll"><i></i></span>
    </ul>
    <div class="service-body">
      <h3>MÄNNERVORSORGE</h3>
      <p class="intro">Sed ut perspiciatis unde omnis iste natus error sit voluptatem accusantium doloremque laudantium, totam rem aperiam, eaque ipsa quae ab illo inventore veritatis et quasi architecto beatae vitae dicta sunt explicabo. Nemo enim ipsam voluptatem quia voluptas sit aspernatur aut odit aut fugit, sed quia consequuntur magni dolores eos qui ratione voluptatem sequi nesciunt.</p>
      <p>Qui dolorem ipsum quia dolor sit amet, consectetur, adipisci velit, sed quia non numquam eius modi tempora incidunt ut labore et dolore magnam aliquam quaerat voluptatem.</p>
      <p>Ut enim ad minima veniam, quis nostrum exercitationem ullam corporis suscipit laboriosam, nisi ut aliquid ex ea commodi consequatur? Quis autem vel eum iure reprehenderit qui in ea voluptate velit esse quam nihil molestiae consequatur, vel illum qui dolorem eum fugiat quo voluptas nulla pariatur.</p>
      <div class="service-photo" role="img" aria-label="Foto einer Ärztin im Gespräch mit einem Patienten am Empfang"></div>
    </div>
  </div>
</section>
<div class="abs services-bg"></div>

<section class="abs doctors">
  <h2 class="abs section-title" style="top:56px">UNSERE ÄRZTE</h2>
  <article class="doctor" style="left:111px">
    <div class="portrait"><div role="img" aria-label="Porträtfoto von Lena Horbach"></div></div>
    <h4>Lena Horbach</h4>
    <div class="role">Vice President</div>
    <p>Neque porro quisquam est, qui dolorem ipsum quia dolor sit amet, consectetur, adipisci velit, sed quia non numquam eius modi tempora incidunt ut labore et dolore.</p>
  </article>
  <article class="doctor" style="left:446px">
    <div class="portrait"><div role="img" aria-label="Porträtfoto von Julian.K"></div></div>
    <h4>Julian.K</h4>
    <div class="role">Vice President</div>
    <p>Neque porro quisquam est, qui dolorem ipsum quia dolor sit amet, consectetur, adipisci velit, sed quia non numquam eius modi tempora incidunt ut labore et dolore.</p>
  </article>
  <article class="doctor" style="left:779px">
    <div class="portrait"><div role="img" aria-label="Porträtfoto von Marco Feld"></div></div>
    <h4>Marco Feld</h4>
    <div class="role">Vice President</div>
    <p>Neque porro quisquam est, qui dolorem ipsum quia dolor sit amet, consectetur, adipisci velit, sed quia non numquam eius modi tempora incidunt ut labore et dolore.</p>
  </article>
</section>

<section class="abs hours">
  <div class="hours-bg" role="img" aria-label="Blasses Hintergrundfoto des Praxisgebäudes mit Bäumen"></div>
  <h2 class="abs section-title">ÖFFNUNGSZEITEN</h2>
  <table class="schedule">
    <colgroup><col style="width:161px"><col style="width:163px"><col style="width:162px"><col style="width:164px"><col style="width:161px"><col style="width:165px"></colgroup>
    <tr><th>ZEIT</th><th>MONTAG</th><th>DIENSTAG</th><th>MITTWOCH</th><th>DONNERSTAG</th><th>FREITAG</th></tr>
    <tr><td class="time">AB 7:30</td><td class="c-blood">Blutentnahme/<br>Ultraschall</td><td class="c-blood">Blutentnahme/<br>Ultraschall</td><td class="c-blood">Blutentnahme/<br>Ultraschall</td><td class="c-blood">Blutentnahme/<br>Ultraschall</td><td class="c-blood">Blutentnahme/<br>Ultraschall</td></tr>
    <tr><td class="time">8:00-9:30</td><td class="c-free">Freie<br>Sprechstunde</td><td class="c-free">Freie<br>Sprechstunde</td><td class="c-free">Freie<br>Sprechstunde</td><td class="c-free">Freie<br>Sprechstunde</td><td class="c-free">Freie<br>Sprechstunde</td></tr>
    <tr><td class="time">9:00-10:00</td><td class="c-free">Freie<br>Sprechstunde</td><td class="c-free">Freie<br>Sprechstunde</td><td class="c-free">Freie<br>Sprechstunde</td><td class="c-free">Freie<br>Sprechstunde</td><td class="c-free">Freie<br>Sprechstunde</td></tr>
    <tr><td class="time">10:00-11:00</td><td class="c-free">Freie<br>Sprechstunde</td><td class="c-free">Freie<br>Sprechstunde</td><td class="c-free">Freie<br>Sprechstunde</td><td class="c-free">Freie<br>Sprechstunde</td><td class="c-free">Freie<br>Sprechstunde</td></tr>
    <tr><td class="time">11:00-12:00</td><td class="c-free">Freie<br>Sprechstunde</td><td class="c-free">Freie<br>Sprechstunde</td><td class="c-free">Freie<br>Sprechstunde</td><td class="c-free">Freie<br>Sprechstunde</td><td class="c-free">Freie<br>Sprechstunde</td></tr>
    <tr><td class="time">12:00-13:00</td><td class="c-visit">Hausbesuche</td><td class="c-visit">Hausbesuche</td><td class="c-visit">Hausbesuche</td><td class="c-visit">Hausbesuche</td><td class="c-visit">Hausbesuche</td></tr>
    <tr><td class="time">13:00-14:00</td><td class="c-lunch">Mittagspause</td><td class="c-lunch">Mittagspause</td><td class="c-lunch">Mittagspause</td><td class="c-lunch">Mittagspause</td><td class="c-lunch">Mittagspause</td></tr>
    <tr><td class="time">14:00-15:30</td><td class="c-lunch">Mittagspause</td><td class="c-lunch">Mittagspause</td><td class="c-lunch">Mittagspause</td><td class="c-lunch">Mittagspause</td><td class="c-lunch">Mittagspause</td></tr>
    <tr><td class="time">15:30-16:00</td><td class="c-appt">Termin-<br>sprechstunde</td><td class="c-appt">Termin-<br>sprechstunde</td><td class="c-appt">Termin-<br>sprechstunde</td><td class="c-appt">Termin-<br>sprechstunde</td><td class="c-appt">Termin-<br>sprechstunde</td></tr>
    <tr><td class="time">16:00-17:00</td><td class="c-late">Freie<br>Sprechstunde</td><td class="c-late">Freie<br>Sprechstunde</td><td class="c-late"></td><td class="c-late">Freie<br>Sprechstunde</td><td class="c-late"></td></tr>
    <tr><td class="time">17:00-18:00</td><td class="c-late">Freie<br>Sprechstunde</td><td class="c-late">Freie<br>Sprechstunde</td><td class="c-late"></td><td class="c-late">Freie<br>Sprechstunde</td><td class="c-late"></td></tr>
  </table>
</section>

<section class="abs team">
  <div class="team-photo" role="img" aria-label="Freigestelltes Porträtfoto einer Mitarbeiterin in blauer Bluse"></div>
  <h2>TRIFF DAS TEAM</h2>
  <span class="slider-line"></span><span class="slider-dot"></span>
  <span class="arrow prev"><svg width="10" height="12" viewBox="0 0 10 12"><path d="M7 1 2 6l5 5" fill="none" stroke="#fff" stroke-width="2"/></svg></span>
  <span class="arrow next"><svg width="10" height="12" viewBox="0 0 10 12"><path d="M3 1l5 5-5 5" fill="none" stroke="#fff" stroke-width="2"/></svg></span>
  <div class="member">
    <h3>Carla M. Weidner</h3>
    <div class="role">CEO</div>
    <p>But I must explain to you how all this mistaken idea of denouncing pleasure and praising pain was born and I will give you a complete account of the system, and expound the actual teachings of the great explorer of the truth, the master-builder of human happiness.</p>
    <p>No one rejects, dislikes, or avoids pleasure itself, because it is pleasure, but because those who do not know how to pursue pleasure rationally encounter consequences that are extremely painful. Nor again is there anyone who loves or pursues or desires to obtain pain of itself, because it is pain, but because occasionally circumstances occur in which toil and pain can procure him some great pleasure. To take a trivial example, which of us ever undertakes laborious physical exercise, except to obtain some advantage from it.</p>
    <p>But who has any right to find fault with a man who chooses to enjoy a pleasure that has no annoying consequences, or one who avoids a pain that produces.</p>
  </div>
</section>

<footer class="abs footer">
  <h2 style="left:111px">SCHNELLER KONTAKT</h2>
  <h2 style="left:692px">KONTAKT FORMULAR</h2>
  <div class="contact-line" style="left:111px;top:144px"><svg width="11" height="14" viewBox="0 0 11 14"><path d="M5.5 0A5.5 5.5 0 0 0 0 5.5C0 9.5 5.5 14 5.5 14S11 9.5 11 5.5A5.5 5.5 0 0 0 5.5 0zm0 7.5a2 2 0 1 1 0-4 2 2 0 0 1 0 4z" fill="#7386b8"/></svg>Am Lindenhof 14, 48990 Harlen</div>
  <div class="contact-line" style="left:111px;top:170px"><svg width="12" height="11" viewBox="0 0 12 11"><rect x="0" y="3" width="12" height="8" fill="#7386b8"/><rect x="2" y="0" width="8" height="3" fill="#7386b8"/></svg>0123 4567809</div>
  <div class="contact-line" style="left:380px;top:144px"><svg width="12" height="12" viewBox="0 0 12 12"><path d="M2.5 0l2 3-1.3 1.3a7 7 0 0 0 4.5 4.5L9 7.5l3 2-1.5 2.5C5 12 0 7 0 1.5z" fill="#7386b8"/></svg>0123 4567801</div>
  <div class="contact-line" style="left:380px;top:170px"><svg width="12" height="9" viewBox="0 0 12 9"><rect x=".5" y=".5" width="11" height="8" fill="none" stroke="#7386b8"/><path d="M.5.5 6 5l5.5-4.5" fill="none" stroke="#7386b8"/></svg>info@praxis-harlen.de</div>
  <div class="legal" style="left:111px;top:210px">Copyright © 2019. Praxisgemeinschaft Harlen</div>
  <div class="legal" style="left:406px;top:210px">Datenschutz-Bestimmungen</div>
  <div class="legal" style="left:111px;top:235px">Alle Rechte vorbehalten.</div>
  <div class="field" style="left:614px;top:122px;width:232px">Name:</div>
  <div class="field" style="left:856px;top:122px;width:231px">Telefon:</div>
  <div class="field" style="left:614px;top:181px;width:473px">Email:</div>
  <div class="submit">EINREICHEN</div>
</footer>

</body>
</html>
```